Velmora CBD Tincture packaging design

We are seeking a designer to create the label that will be printed on cardboard box packaging, which will carry our CBD tincture. We envision the box being white to resemble a clean look that stands out on shelves. Our logo (attached) uses shades of yellows and greens in the form of a fluid drop resembling half plant and half plant extract. The packaging will show that we only use clean (TRUNK certified) hemp extract thats been extracted using the cleanest method of extraction; supercritical CO2. Our tincture uses a fractionated coconut oil to improve absorption for the consumer, increasing onset time and providing essential omega fatty acids. We take pride in our use of a clean product with a clean extraction. The tincture bottle itself holds 30ml of liquid and is a clear glass bottle. The cap for the tincture bottle is white and has a graduated glass stem that shows the measurements for how much liquid it holds (picture attached). We have not yet done the label that will stick on the tincture, but i image it will be a frosted white label with the Velmora logo and a few words describing the product. This project is for the cardboard box that will hold each individual tincture bottle.

BOX DIMENSIONS: 1.31" x 1.31" x 4.13" (LxWxH)

We will be releasing a new product (cbd capsules) in April, and we will reach out to the designer of this product as first option to create the design for the capsule packaging.

Target Market(s)

convenience stores, medical marijuana dispensaries, health stores

Font styles to use
Serif

Colors
ffffff
fbed22
ffc214
ffcf3e
acd136
9bcb3c

Requirements
Must have
• -Velmora company logo
-Made with full spectrum supercritical CO2 Hemp Extract
-Made from TRUNK certified clean hemp
-Declaration of ingredients (fractionated coconut oil, CBD hemp extract)
-1200mg CBD Tincture
-Nt. Wt. 1FL OZ (30ml)
-These statements have not been evaluated by the Food and Drug Administration. FDA has not evaluated this product for safety or efficacy. This product is not intended to diagnose, treat, cure or prevent any disease.
-DO NOT REFRIGERATE. Keep at room temperature to preserve freshness. Store away from humidity, heat, and light. Warning: If pregnant, nursing or taking prescription drugs, consult your physician prior to use. Keep out of reach of children.
-Manufactured by Velmora CBD Co. 58 Quarry Bend Rd. Scarborough, ME 04019
-Batch ID:___________
-Expiration Date:____________
-Good Manufacturing Practice (GMP) Logo
-TRUNK logo
Nice to have
• -Contains omega 3, 6 and essential fatty acids
-Graduated dropper for precise dosing
-40mg of CBD per dropper!
-Made in the USA
-No Pesticides
-No Solvents
-No Heavy Metals
-CO2 Extraction
-3rd Party Lab Tested

```html
<!DOCTYPE html>
<html lang="en">
<head>
<meta charset="utf-8">
<title>Velmora CBD Tincture – Box Panels</title>
<link rel="stylesheet" href="https://fonts.googleapis.com/css2?family=Nunito:wght@500&family=Roboto+Condensed:wght@400;700&family=Roboto:wght@400;500&display=swap">
<style>
  :root {
    --canvas: #d9d8d3;
    --panel-white: #ffffff;
    --cream: #f6f4df;
    --leaf-green: #9bcb3c;
    --lime: #acd136;
    --deep-green: #1f7a1f;
    --text-dark: #2b2b2b;
    --gold: #ffcf3e;
    --gold-deep: #ffc214;
    --amber: #e89a2c;
    --rust: #c8651b;
    --badge-green: #5aa83a;
  }
  * { margin: 0; padding: 0; box-sizing: border-box; }
  html, body { width: 1200px; height: 900px; overflow: hidden; }
  body { background: var(--canvas); font-family: "Roboto", sans-serif; }

  .box-flat {
    position: absolute; left: 334px; top: 30px;
    width: 532px; height: 840px; display: flex;
    box-shadow: 0 6px 24px rgba(0,0,0,.15);
  }
  .panel { position: relative; width: 266px; height: 840px; overflow: hidden; background: var(--panel-white); }
  .panel + .panel { border-left: 1px solid #e6e4da; }
  .panel-bg { position: absolute; inset: 0; }

  .brand { position: absolute; left: 0; right: 0; text-align: center; font-family: "Nunito", sans-serif; font-weight: 500; color: var(--text-dark); }
  .brand-dot { display: block; margin: 0 auto 10px; border-radius: 50%; background: var(--gold-deep); }

  .product-type { position: absolute; color: var(--deep-green); font-family: "Roboto Condensed", sans-serif; }
  .product-type .spectrum { display: block; font-weight: 400; }
  .product-type .name { display: block; font-weight: 700; line-height: .95; letter-spacing: .5px; }
  .strength-band {
    position: absolute; left: 0; right: 0; color: var(--deep-green);
    font-family: "Roboto", sans-serif; font-weight: 500; text-align: center;
    background: linear-gradient(90deg, rgba(255,207,62,.25), var(--gold) 30%, var(--gold) 70%, rgba(255,207,62,.25));
  }

  /* front panel */
  .front .brand { top: 196px; font-size: 50px; letter-spacing: -.5px; line-height: 1.1; }
  .front .brand-dot { width: 44px; height: 44px; }
  .front .product-type { left: 24px; top: 452px; }
  .front .spectrum { font-size: 27px; }
  .front .name { font-size: 54px; }
  .front .strength-band { top: 556px; height: 30px; line-height: 30px; font-size: 16px; }
  .claims {
    position: absolute; left: 30px; top: 636px; list-style: none;
    border-left: 2px solid var(--deep-green); padding-left: 6px;
    color: var(--deep-green); font-family: "Roboto Condensed", sans-serif; font-size: 15px; line-height: 23px;
  }
  .ripple-art { position: absolute; left: 40px; right: 40px; top: 738px; height: 62px; border-radius: 50%; }
  .net-wt { position: absolute; bottom: 20px; left: 0; right: 0; text-align: center; color: #fff; font-family: "Roboto Condensed", sans-serif; font-size: 16px; }

  /* side panel */
  .badge { position: absolute; border-radius: 50%; border: 3px solid var(--badge-green); background: #fff; }
  .badge-gmp { top: 18px; left: 14px; width: 56px; height: 56px; }
  .badge-trunk { bottom: 70px; right: 14px; width: 52px; height: 52px; }
  .side .brand { top: 60px; font-size: 26px; }
  .side .brand-dot { width: 22px; height: 22px; margin-bottom: 6px; }
  .side .product-type { left: 0; right: 0; top: 160px; text-align: center; }
  .side .spectrum { font-size: 15px; }
  .side .name { font-size: 36px; }
  .side .strength-band { top: 222px; height: 20px; line-height: 20px; font-size: 11px; background: none; }
  .fine-print {
    position: absolute; left: 16px; right: 16px; top: 360px;
    color: var(--text-dark); font-size: 8.6px; line-height: 1.38;
  }
  .fine-print p { margin-bottom: 8px; }
  .fine-print strong { font-weight: 500; }
  .made-in { position: absolute; bottom: 30px; right: 14px; color: #fff; font-family: "Roboto Condensed", sans-serif; font-size: 11px; }
</style>
</head>
<body>
<main class="box-flat">

  <section class="panel side">
    <svg class="panel-bg" viewBox="0 0 266 840" preserveAspectRatio="none" aria-hidden="true">
      <defs>
        <linearGradient id="sideFade" x1="0" y1="0" x2="0" y2="1">
          <stop offset="0" stop-color="#ffffff"/>
          <stop offset=".55" stop-color="#fbfaf0"/>
          <stop offset=".8" stop-color="#f6e7b4"/>
          <stop offset=".92" stop-color="#e89a2c"/>
          <stop offset="1" stop-color="#c8651b"/>
        </linearGradient>
      </defs>
      <path d="M0 330 C60 290 150 250 266 262 L266 840 L0 840 Z" fill="url(#sideFade)"/>
      <path d="M0 330 C60 290 150 250 266 262 L266 276 C160 268 70 300 0 346 Z" fill="var(--lime)"/>
    </svg>
    <div class="badge badge-gmp" role="img" aria-label="GMP certification badge"></div>
    <div class="brand"><span class="brand-dot"></span>Velmora</div>
    <div class="product-type"><span class="spectrum">Full spectrum</span><span class="name">HEMP OIL</span></div>
    <div class="strength-band">1200mg CBD Tincture</div>
    <div class="fine-print">
      <p><strong>Ingredients :</strong> Made with full spectrum supercritical CO2 Hemp Extract. Made from TRUNK certified clean hemp. Fractionated coconut oil, CBD hemp extract. Contains omega 3, 6 and essential fatty acids.</p>
      <p><strong>Caution :</strong> These statements have not been evaluated by the Food and Drug Administration. FDA has not evaluated this product for safety or efficacy. This product is not intended to diagnose, treat, cure or prevent any disease.</p>
      <p><strong>DO NOT REFRIGERATE.</strong> Keep at room temperature to preserve freshness. Store away from humidity, heat, and light. Warning: If pregnant, nursing or taking prescription drugs, consult your physician prior to use. Keep out of reach of children.</p>
      <p><strong>Manufactured by :</strong> Velmora CBD Co. 58 Quarry Bend Rd. Scarborough, ME 04019</p>
      <p>Batch ID:___________</p>
      <p>Expiration Date:____________</p>
    </div>
    <div class="badge badge-trunk" role="img" aria-label="TRUNK certification badge"></div>
    <div class="made-in">Made in the USA</div>
  </section>

  <section class="panel front">
    <svg class="panel-bg" viewBox="0 0 266 840" preserveAspectRatio="none" aria-hidden="true">
      <defs>
        <linearGradient id="frontFade" x1="0" y1="0" x2="0" y2="1">
          <stop offset="0" stop-color="#f7f8e6"/>
          <stop offset=".35" stop-color="#fbfaf0"/>
          <stop offset=".6" stop-color="#fbf3d2"/>
          <stop offset=".8" stop-color="#f2c46a"/>
          <stop offset=".92" stop-color="#e08a2a"/>
          <stop offset="1" stop-color="#c8651b"/>
        </linearGradient>
      </defs>
      <path d="M0 366 C70 326 170 366 266 424 L266 840 L0 840 Z" fill="url(#frontFade)"/>
      <path d="M0 350 C70 310 170 352 266 408 L266 424 C170 366 70 326 0 366 Z" fill="var(--lime)"/>
    </svg>
    <div class="brand"><span class="brand-dot"></span>Velmora</div>
    <div class="product-type"><span class="spectrum">Full spectrum</span><span class="name">HEMP OIL</span></div>
    <div class="strength-band">1200mg CBD Tincture</div>
    <ul class="claims">
      <li>No Pesticides</li>
      <li>No Solvents</li>
      <li>CO2 Extraction</li>
      <li>No Heavy Metals</li>
    </ul>
    <div class="ripple-art" role="img" aria-label="Golden oil drop falling into a rippling pool of oil"
         style="background: radial-gradient(ellipse at center, #ffcf3e 0%, #e8a23a 45%, rgba(200,101,27,0) 75%);"></div>
    <div class="net-wt">Nt. Wt. 1FL OZ (30ml)</div>
  </section>

</main>
</body>
</html>
```